Meadowlark Counseling Partners, LLC Needs Modern Business Card Design.

We provide behavioral health services from western Kansas to eastern Kansas. There is an abundance of competition for the services we provide with our main competitor being larger and having significantly more financial resources; however, the quality of services we provide is greater and we have started to catch the attention of the State of Kansas. We had a great logo designed by ArtFolio - this will be used to build upon our brand. The logo (attached) should be used in the card development. We want something unique, modern, but also a card design that clearly states our name, contact info, provides the name and unqiue location of each clinician, etc. Rounded edges, or a unique size, just something that makes our business card stand out from others. I have also uploaded each clinician's name and their unique location and phone number.

Our idea is to have one side be black with our logo. Then, on the other side have business cards for each individual. Plus, we want one card that is "generic" with no specific clinician's name listed so that we can give clients an appointment card when they leave. Some clinicians have two locations - we're open to design and background color, but we have started going with branding colors of black, the yellow in the logo files attached, and sometimes a gray. Our new office has been decorated using this theme.

Target Market(s)

individuals and families in need of behavioral health services; potential professional referral sources; existing referral sources

Industry/Entity Type

Business

Contact Information for Business Card

I attached a Word doc that provides clinician names, credentials and location information specific to each individual.

Font styles to use
Serif

Colors
000000
fbed22
dbdbdb
9d9d9d
c3c3c3

Requirements
Must have
• 1) use of the company logo that has been attached; 2) a template that provides us space to individualize business cards for all of our clinicians; 3) should stick to the colors we are branding with: black, yellow from the logo file, maybe a gray shade and we're open to a suggestion on a shade of white.
Nice to have
• Group discussion culminated in the thought that one side would be black with just our logo - no clinician names, etc. A unique design - rounded edges, unique size, some catchy lay-out would be nice.
Should not have
• Must not be too busy. Should look "clean." The project should stick to branding colors: black, yellow (from the logo file), maybe a gray and shade of white.

```html
<!DOCTYPE html>
<html lang="en">
<head>
<meta charset="utf-8">
<title>Meadowlark Counseling Partners – Business Card</title>
<link rel="stylesheet" href="https://fonts.googleapis.com/css2?family=Libre+Baskerville:wght@400;700&display=swap">
<style>
  :root {
    --ink: #0b0b0b;
    --gold: #f3b62a;
    --gold-soft: #e7a91f;
    --backdrop: #e4e4e4;
    --paper-text: #f1f1f1;
  }
  * { box-sizing: border-box; margin: 0; padding: 0; }
  html, body { width: 1200px; height: 750px; overflow: hidden; }
  body {
    background: var(--backdrop);
    font-family: "Libre Baskerville", Georgia, serif;
    position: relative;
  }
  .card {
    position: absolute;
    background: var(--ink);
    border-radius: 6px;
    overflow: hidden;
    box-shadow: 0 10px 28px rgba(0,0,0,0.22);
  }

  /* Personal side (portrait) */
  .card-personal { left: 110px; top: 78px; width: 340px; height: 595px; }
  .card-personal .top-band { position: absolute; left: 0; top: 0; width: 340px; height: 220px; }
  .brand-block {
    position: absolute; left: 0; top: 46px; width: 340px;
    display: flex; flex-direction: column; align-items: center; gap: 10px;
  }
  .brand-mark { width: 30px; height: 30px; border-radius: 50%; background: var(--ink); }
  .brand-name {
    color: var(--ink); font-weight: 700; text-align: center;
    text-transform: uppercase; line-height: 1.35;
  }
  .brand-name .line-1 { display: block; font-size: 20px; letter-spacing: 2px; }
  .brand-name .line-2 { display: block; font-size: 9.5px; letter-spacing: 1px; }

  .holder { position: absolute; left: 36px; top: 246px; color: var(--gold); }
  .holder-name { font-size: 21px; letter-spacing: 1px; text-transform: uppercase; }
  .holder-title { font-size: 15px; font-weight: 700; margin-top: 8px; margin-left: 86px; }

  .contact-rail { position: absolute; left: 0; top: 318px; width: 340px; height: 40px; }
  .contact-list {
    position: absolute; left: 96px; top: 372px; list-style: none;
    color: var(--paper-text); font-size: 12px; line-height: 26px;
  }
  .address-rail { position: absolute; left: 0; top: 478px; width: 340px; height: 40px; }
  .address {
    position: absolute; left: 0; top: 526px; width: 340px; text-align: center;
    color: var(--gold); font-size: 12.5px; line-height: 20px;
  }

  /* Logo side (landscape) */
  .card-logo { left: 520px; top: 205px; width: 595px; height: 340px; }
  .card-logo .edge-bands { position: absolute; inset: 0; width: 595px; height: 340px; }
  .logo-block {
    position: absolute; left: 150px; top: 86px; width: 340px;
    display: flex; flex-direction: column; align-items: center; gap: 14px;
  }
  .logo-block .brand-mark { width: 46px; height: 46px; background: var(--gold); }
  .logo-block .brand-name { color: var(--gold); }
  .logo-block .brand-name .line-1 { font-size: 32px; letter-spacing: 3px; }
  .logo-block .brand-name .line-2 { font-size: 13px; letter-spacing: 1.5px; }
  .logo-rule { width: 300px; height: 2px; background: var(--gold); }
</style>
</head>
<body>

  <section class="card card-personal" aria-label="Clinician side of business card">
    <svg class="top-band" viewBox="0 0 340 220" aria-hidden="true">
      <path d="M0 0 H340 V132 Q190 150 0 212 Z" fill="var(--gold)"/>
    </svg>

    <div class="brand-block">
      <span class="brand-mark"></span>
      <p class="brand-name">
        <span class="line-1">Meadowlark</span>
        <span class="line-2">Counseling Partners, LLC</span>
      </p>
    </div>

    <div class="holder">
      <h1 class="holder-name">Harlan J. Reede, LP</h1>
      <p class="holder-title">President</p>
    </div>

    <svg class="contact-rail" viewBox="0 0 340 40" aria-hidden="true">
      <g fill="none" stroke="var(--gold)" stroke-width="1.4">
        <line x1="0" y1="20" x2="300" y2="20"/>
        <g fill="var(--ink)">
          <circle cx="110" cy="20" r="10"/>
          <circle cx="160" cy="20" r="10"/>
          <circle cx="210" cy="20" r="10"/>
          <circle cx="260" cy="20" r="10"/>
        </g>
      </g>
      <!-- phone -->
      <path d="M106 15 q-1 0 -1 2 q1 6 8 8 q2 0 2 -1 l0 -2 l-3 -1 l-1 1 q-3 -1 -4 -4 l1 -1 l-1 -3 Z" fill="var(--gold)"/>
      <!-- fax -->
      <g fill="var(--gold)">
        <rect x="156" y="14" width="8" height="4"/>
        <rect x="154" y="18" width="12" height="6" rx="1"/>
      </g>
      <!-- email -->
      <g fill="none" stroke="var(--gold)" stroke-width="1.4">
        <rect x="204" y="15.5" width="12" height="9"/>
        <path d="M204 15.5 L210 21 L216 15.5"/>
        <!-- web -->
        <circle cx="260" cy="20" r="5.5"/>
        <line x1="254.5" y1="20" x2="265.5" y2="20"/>
        <ellipse cx="260" cy="20" rx="2.4" ry="5.5"/>
      </g>
    </svg>

    <ul class="contact-list">
      <li>(316) 555-0142</li>
      <li>(316) 555-0142</li>
      <li>hello@meadowlarkcp.com</li>
      <li>www.meadowlarkcp.com</li>
    </ul>

    <svg class="address-rail" viewBox="0 0 340 40" aria-hidden="true">
      <g fill="none" stroke="var(--gold)" stroke-width="1.4">
        <line x1="0" y1="20" x2="158" y2="20"/>
        <line x1="182" y1="20" x2="300" y2="20"/>
        <polyline points="300,20 316,6 340,6"/>
        <circle cx="170" cy="20" r="11" fill="var(--ink)"/>
      </g>
      <path d="M170 13 a4.5 4.5 0 0 1 4.5 4.5 c0 3.5 -4.5 8 -4.5 8 s-4.5 -4.5 -4.5 -8 a4.5 4.5 0 0 1 4.5 -4.5 Z" fill="var(--gold)"/>
      <circle cx="170" cy="17.5" r="1.6" fill="var(--ink)"/>
    </svg>

    <address class="address">
      418 N. Elmwood Ave.<br>
      Wichita, Kansas 67208
    </address>
  </section>

  <section class="card card-logo" aria-label="Logo side of business card">
    <svg class="edge-bands" viewBox="0 0 595 340" aria-hidden="true">
      <path d="M0 0 H46 Q30 170 40 340 H0 Z" fill="var(--gold)"/>
      <path d="M56 0 Q40 170 50 340" fill="none" stroke="var(--gold-soft)" stroke-width="1.5"/>
      <path d="M585 0 H595 V340 H580 Q588 170 585 0 Z" fill="var(--gold)"/>
    </svg>

    <div class="logo-block">
      <span class="brand-mark"></span>
      <p class="brand-name">
        <span class="line-1">Meadowlark</span>
        <span class="line-2">Counseling Partners, LLC</span>
      </p>
      <span class="logo-rule"></span>
    </div>
  </section>

</body>
</html>
```